Larkfield Circuitry LLC is a Minneapolis / St Paul and surrounding communities computer repair and service company. It serves residential and small businesses. We work primarily with virus removal, data recovery, system baselines, networking, and new system installation. The site should look clean, professional, and easy to navigate.

This wordpress project must be coded and integrated into a wordpress theme for easy upload and maintenance.
Updates

Designers - Please make sure your design is in a wordpress theme so that It can be uploaded.  

Thank you,

Brin 

Target Market(s)

Residential and Small Business

Industry/Entity Type

Residential

Requirements
Must have
• Site Content
1. Main Page should have photos that scroll across, Business Description, Space to run
“Specials” Ads
a. Intuitive Navigation
2. Additional Pages
a. Blog for Computer Repair Articles
b. Testimonials Page
c. Contact Pages
d. Services Page with the ability to put in pricing
3. The site must be clean and professional.
4. Wordpress Theme

```html
<!DOCTYPE html>
<html lang="en">
<head>
<meta charset="utf-8">
<title>Larkfield Circuitry LLC</title>
<link rel="stylesheet" href="https://fonts.googleapis.com/css2?family=Arimo:wght@400;700&family=PT+Serif&family=Open+Sans:wght@700&display=swap">
<style>
:root{
  --page:#e8f4fb;
  --top-a:#0a8ad8;
  --top-b:#0b67ab;
  --navband:#9fc0d5;
  --ink:#111;
  --body:#2f5466;
  --heading:#0b4a72;
  --sub:#1a6c9e;
  --lead:#4a8a00;
  --orange:#f26a10;
  --hero-a:#0f7aa6;
  --hero-b:#064f78;
  --hero-band:#2aa8cd;
  --box-line:#c9d9e3;
  --blue-a:#9fc0d8;
  --blue-b:#5b8db6;
  --green-a:#93cc44;
  --green-b:#4b9a19;
  --orange-a:#e2661c;
  --orange-b:#c2460a;
  --footer:#00324a;
  --white:#fff;
}
*{box-sizing:border-box;margin:0;padding:0}
html,body{width:1026px;height:1200px;overflow:hidden}
body{position:relative;background:var(--page);font-family:"Arimo",Arial,sans-serif;color:var(--ink)}
.abs{position:absolute}
.topbar{left:0;top:0;width:1026px;height:62px;background:linear-gradient(var(--top-a),var(--top-b))}
.navband{left:0;top:62px;width:1026px;height:37px;background:var(--navband);border-top:1px solid #7ea5bf}
.logo-card{left:18px;top:0;width:186px;height:130px;background:var(--white);border-radius:0 0 6px 6px;box-shadow:0 3px 6px rgba(0,40,80,.35);display:flex;align-items:center;justify-content:center;gap:7px;padding:0 10px}
.logo-dot{width:22px;height:22px;border-radius:50%;background:#4c9a2a;flex:none}
.logo-name{font-family:"Arimo",Arial,sans-serif;font-weight:700;font-size:16px;line-height:19px;color:#3a3a3a}
.main-nav{left:232px;top:70px;height:29px;display:flex;font-size:13px}
.main-nav a{color:var(--ink);text-decoration:none;line-height:30px}
.main-nav .current{background:var(--page);width:84px;text-align:center;border-radius:3px 3px 0 0}
.hero{left:17px;top:141px;width:990px;height:336px;background:radial-gradient(circle at 70% 30%,#1a8cb8,var(--hero-a) 40%,var(--hero-b));overflow:hidden}
.hero-band{left:0;top:296px;width:990px;height:40px;background:var(--hero-band)}
.hero-title{left:50px;top:36px;font-family:"Open Sans",Verdana,sans-serif;font-weight:700;font-size:31px;color:var(--orange)}
.hero-list{left:75px;top:96px;font-family:"Open Sans",Verdana,sans-serif;font-weight:700;font-size:21px;line-height:30px;color:var(--white);list-style:none}
.hero-cta{left:338px;top:138px;width:217px;height:49px;background:linear-gradient(#39b3dc,#0f6fa0);border-radius:3px;box-shadow:2px 3px 4px rgba(0,0,0,.35);color:var(--white);font-family:"Open Sans",Verdana,sans-serif;font-weight:700;font-size:18px;display:flex;align-items:center;padding-left:20px;gap:16px}
.hero-photo{left:530px;top:55px;width:325px;height:265px;background:linear-gradient(#3a3f48,#9aa1aa);border-radius:6px}
.box{background:var(--white);border:1px solid var(--box-line);border-radius:3px}
.box-head{height:32px;margin:3px;color:var(--white);font-family:"PT Serif",Georgia,serif;font-size:20px;line-height:32px;padding-left:9px}
.head-blue{background:linear-gradient(var(--blue-a),var(--blue-b))}
.head-green{background:linear-gradient(var(--green-a),var(--green-b))}
.head-orange{background:linear-gradient(var(--orange-a),var(--orange-b))}
.field-row{display:flex;align-items:center;justify-content:space-between;padding:0 12px 0 12px;font-size:12px;font-weight:700;color:#0a2a3a}
.field{width:95px;height:21px;border:1px solid #8aa0ad;background:var(--white)}
.btn{display:inline-block;color:var(--white);font-size:12px;line-height:15px;padding:0 6px;border-radius:4px}
.btn-dark{background:#0b3a52}
.btn-green{background:#3f7a12}
.btn-rust{background:#9a3a0a}
.more{display:flex;width:54px;height:12px;border-radius:3px;overflow:hidden;font-size:8px;font-weight:700;color:var(--white);line-height:12px}
.more span{background:#3d8a12;flex:1;text-align:center;letter-spacing:.5px}
.more i{background:#0b3a66;width:13px;display:flex;align-items:center;justify-content:center}
.welcome{left:221px;top:496px;font-size:37px;color:var(--heading)}
.copy{font-size:14px;line-height:20px;color:var(--body)}
.copy b{color:var(--lead)}
.subhead{left:219px;top:639px;font-size:24px;color:var(--sub)}
.rule{border-top:1px dotted #8aa4b2;height:0}
.side-copy{font-size:14px;line-height:20px;color:var(--body);padding:0 8px}
.footer{left:0;top:1064px;width:1026px;height:136px;background:var(--footer)}
.foot-nav a{position:absolute;top:1090px;color:var(--white);font-size:13px;text-decoration:none}
.legal{left:0;top:1126px;width:1054px;text-align:center;color:var(--white);font-size:12px}
</style>
</head>
<body>
<div class="abs topbar"></div>
<div class="abs navband"></div>

<div class="abs logo-card">
  <span class="logo-dot"></span>
  <span class="logo-name">Larkfield Circuitry LLC</span>
</div>

<nav class="abs main-nav">
  <a class="current" href="#">HOME</a>
  <a href="#" style="margin-left:20px">TESTIMONIALS</a>
  <a href="#" style="margin-left:33px">SERVICES</a>
  <a href="#" style="margin-left:46px">PROJECTS</a>
  <a href="#" style="margin-left:38px">SOLUTIONS</a>
  <a href="#" style="margin-left:46px">CONTACT US</a>
</nav>

<section class="abs hero">
  <div class="abs hero-band"></div>
  <h2 class="abs hero-title">Our services</h2>
  <ul class="abs hero-list">
    <li>Virus removal,</li>
    <li>Data recovery,</li>
    <li>System baselines,</li>
    <li>Networking, and</li>
    <li>New system installation.</li>
  </ul>
  <a class="abs hero-cta">Get In Touch
    <svg width="40" height="22" viewBox="0 0 40 22"><path d="M0 7h26V0l14 11-14 11v-7H0z" fill="#0b4a72"/></svg>
  </a>
  <div class="abs hero-photo" role="img" aria-label="Open silver laptop computer"></div>
</section>

<!-- Left sidebar -->
<aside class="abs box" style="left:16px;top:500px;width:190px;height:137px">
  <div class="box-head head-blue">Members log in</div>
  <div class="field-row" style="margin-top:14px">Name:<span class="field"></span></div>
  <div class="field-row" style="margin-top:9px">Password:<span class="field"></span></div>
  <div class="field-row" style="margin-top:7px;font-size:10px;font-weight:400;letter-spacing:.5px;padding-right:13px">A REGISTERED MEMBER?<span class="btn btn-dark">go</span></div>
</aside>

<aside class="abs box" style="left:16px;top:651px;width:190px;height:112px">
  <div class="box-head head-green">Newsletter signup</div>
  <div class="field-row" style="margin-top:15px">Email id:<span class="field"></span></div>
  <div style="text-align:right;padding-right:13px;margin-top:8px"><span class="btn btn-green">go</span></div>
</aside>

<aside class="abs box" style="left:16px;top:778px;width:190px;height:269px">
  <div class="box-head head-orange">Contact info</div>
  <div class="field-row" style="margin-top:14px">Your name:<span class="field"></span></div>
  <div class="field-row" style="margin-top:6px">Address:<span class="field"></span></div>
  <div class="field-row" style="margin-top:6px">Email id:<span class="field"></span></div>
  <div class="field-row" style="margin-top:6px">Zip code:<span class="field"></span></div>
  <div class="field-row" style="margin-top:6px;align-items:flex-start">Comments:<span class="field" style="height:71px"></span></div>
  <div style="text-align:right;padding-right:13px;margin-top:10px"><span class="btn btn-rust">submit</span></div>
</aside>

<!-- Main content -->
<h1 class="abs welcome">Welcome To Our Site</h1>
<p class="abs copy" style="left:220px;top:552px;width:585px"><b>Lorem ipsum dolor sit amet</b>, consectetuer adipiscing elit. Praesent adipiscing ipsid nislpo. Praesent quis magna vel neque porttitor mollis. In eleifend, risus et hendrerit tempor, purusur imperdiet augu, at ullamcorper eros magna id mauris.Nunc justo lects, luctus vitae, porttito at, fermentum sit amet, ante.</p>
<h2 class="abs subhead" style="font-weight:400">porttito at fermentum sit amet ante magna idetu</h2>
<div class="abs rule" style="left:220px;top:690px;width:485px"></div>
<div class="abs more" style="left:705px;top:684px"><span>MORE</span><i><svg width="7" height="7" viewBox="0 0 7 7"><path d="M0 3h4V1l3 2.5L4 6V4H0z" fill="#fff"/></svg></i></div>
<p class="abs copy" style="left:220px;top:714px;width:560px"><b>Lorem ipsum dolor sit amet</b>, consectetuer adipiscing elit. Praesent adipiscing ipsid nislpo. Praesent quis magna vel neque porttitor mollis. In eleifend, risus et hendrerit tempor, purusur imperdiet augu, at ullamcorper eros magna id mauris.Nunc justo lects, luctus vitae, porttito at, fermentum sit amet, ante.</p>
<div class="abs rule" style="left:220px;top:820px;width:576px"></div>
<div class="abs" style="left:511px;top:830px;width:1px;height:208px;background:#b9cad4"></div>
<div class="abs" role="img" aria-label="Desktop computer with monitor, tower and keyboard" style="left:232px;top:840px;width:222px;height:155px;background:linear-gradient(#2a2f36,#6d7680);border-radius:4px"></div>
<div class="abs" role="img" aria-label="Compact desktop computer with widescreen monitor" style="left:572px;top:838px;width:208px;height:138px;background:linear-gradient(#1e2329,#5d6670);border-radius:4px"></div>

<!-- Right sidebar -->
<aside class="abs box" style="left:815px;top:500px;width:190px;height:360px">
  <div class="box-head head-blue">Testimonials</div>
  <p class="side-copy" style="margin-top:10px">consectetuer adipiscing elit. Praesent adipiscing ipsid nislpo. Praesent quis magna vel neque porttitor mollis.</p>
  <p class="side-copy" style="margin-top:20px">In eleifend, risus et hendrerit tempor, purusur imperdiet augu, at ullamcorper eros magna id mauris.</p>
  <p class="side-copy" style="margin-top:20px">Nunc justo lects, luctus vitae, porttito at, fermentum sit amet, ante.</p>
</aside>

<aside class="abs box" style="left:815px;top:876px;width:190px;height:171px">
  <div class="box-head head-green">More Information</div>
  <p class="side-copy" style="margin-top:11px">Nunc justo lects, luctus vitae, porttito at, fermentum sit amet, ante.</p>
  <div class="abs more" style="left:120px;top:148px"><span>MORE</span><i><svg width="7" height="7" viewBox="0 0 7 7"><path d="M0 3h4V1l3 2.5L4 6V4H0z" fill="#fff"/></svg></i></div>
</aside>

<footer class="abs footer"></footer>
<nav class="foot-nav">
  <a href="#" style="left:196px">HOME</a>
  <a href="#" style="left:273px">TESTIMONIALS</a>
  <a href="#" style="left:397px">SERVICES</a>
  <a href="#" style="left:503px">PROJECTS</a>
  <a href="#" style="left:602px">SOLUTIONS</a>
  <a href="#" style="left:719px">CONTACT US</a>
</nav>
<p class="abs legal">©Larkfield Circuitry 2012 all right reaserved</p>
</body>
</html>
```